Letterhead for Dane Holloway

I need a letterhead based on the business card design

Industry/Entity Type

Business

Requirements
Must have
• Footer: Dane Holloway Naturopath
Shop 3042c, 451 Marrow Lane, Sydney 2000

```html
<!DOCTYPE html>
<html lang="en">
<head>
<meta charset="utf-8">
<title>Dane Holloway Naturopath – Stationery</title>
<link href="https://fonts.googleapis.com/css2?family=Montserrat:wght@400;500&family=Hind:wght@400&family=Nothing+You+Could+Do&display=swap" rel="stylesheet">
<style>
  :root {
    --canvas-bg: #f1f1f1;
    --paper: #ffffff;
    --paper-edge: #e4e4e4;
    --orange: #f0923a;
    --orange-deep: #e97f22;
    --peach: #f6b277;
    --peach-soft: #fbe1c8;
    --ink: #4a4a4a;
    --ink-soft: #6d6d6d;
    --rule: #3c3c3c;
  }
  * { box-sizing: border-box; margin: 0; padding: 0; }
  html, body {
    width: 1200px; height: 1000px; overflow: hidden;
    background: var(--canvas-bg);
  }
  .canvas {
    position: relative; width: 1200px; height: 1000px;
    display: flex; justify-content: center; align-items: center; gap: 40px;
  }
  .page {
    position: relative; width: 540px; height: 764px;
    background: var(--paper);
    border: 1px solid var(--paper-edge);
    overflow: hidden;
  }

  /* Shared wordmark */
  .wordmark {
    display: flex; align-items: center; gap: 8px;
    font-family: "Montserrat", sans-serif; font-weight: 500;
    color: var(--orange); letter-spacing: 0.04em; text-transform: uppercase;
  }
  .wordmark__dot {
    width: 10px; height: 10px; border-radius: 50%; background: var(--orange);
  }

  /* Folder cover */
  .cover__leaves {
    position: absolute; left: 0; top: 0; width: 290px; height: 560px;
    background: linear-gradient(160deg, var(--peach-soft) 0%, var(--peach) 55%, var(--orange) 100%);
    border-radius: 0 70% 60% 0 / 0 40% 60% 0;
    opacity: 0.9;
  }
  .cover__wordmark {
    position: absolute; right: 40px; bottom: 70px; font-size: 15px;
  }

  /* Letterhead */
  .letter__leaf {
    position: absolute; left: 0; top: 70px; width: 250px; height: 470px;
    background: linear-gradient(165deg, #fdf0e3 0%, var(--peach-soft) 60%, #f9d3ae 100%);
    border-radius: 0 70% 60% 0 / 0 40% 60% 0;
    opacity: 0.8;
  }
  .letter__wordmark {
    position: absolute; right: 60px; top: 78px; font-size: 17px;
  }
  .letter__body {
    position: absolute; left: 70px; right: 40px; top: 140px;
    font-family: "Hind", sans-serif; font-size: 9.5px; line-height: 1.5;
    color: var(--ink);
  }
  .letter__body p { margin-bottom: 12px; }
  .letter__signature {
    position: absolute; right: 70px; bottom: 140px;
    font-family: "Nothing You Could Do", cursive; font-size: 24px; color: #2d2d2d;
  }
  .letter__footer {
    position: absolute; left: 40px; right: 40px; bottom: 50px;
    border-top: 1px solid var(--rule); padding-top: 10px; text-align: center;
  }
  .footer__name {
    font-family: "Montserrat", sans-serif; font-weight: 500; font-size: 10px;
    color: var(--orange);
  }
  .footer__details {
    margin-top: 4px; display: flex; justify-content: center; align-items: center; gap: 5px;
    font-family: "Hind", sans-serif; font-size: 8.5px; color: var(--ink-soft);
  }
  .footer__icon { width: 9px; height: 9px; flex: none; }
  .footer__social {
    width: 8px; height: 8px; border-radius: 50%; background: var(--orange); flex: none;
  }
</style>
</head>
<body>
<main class="canvas">

  <section class="page cover" aria-label="Folder cover">
    <div class="cover__leaves" role="img" aria-label="Illustration of overlapping translucent orange leaves"></div>
    <div class="wordmark cover__wordmark"><span class="wordmark__dot"></span>Dane Holloway</div>
  </section>

  <section class="page letter" aria-label="Letterhead">
    <div class="letter__leaf" role="img" aria-label="Faint illustration of pale orange leaves"></div>
    <div class="wordmark letter__wordmark"><span class="wordmark__dot"></span>Dane Holloway</div>

    <div class="letter__body">
      <p>Dear Client,</p>
      <p>Thank you for choosing our clinic for your wellbeing. This letter confirms the details of your first consultation and outlines what you can expect from the visit. Please bring any recent test results, a list of current supplements and medications, and a few notes about your sleep, diet and energy levels. The session runs for about an hour and includes a full health history.</p>
      <p>After the visit we will prepare a tailored plan that may include herbal remedies, flower essences and simple changes to daily routine. Each recommendation is explained clearly so you can follow it with confidence at home.</p>
      <p>If you need to change your appointment, please contact the clinic at least one day ahead. We look forward to working with you and supporting your health.</p>
      <p>Best regards,</p>
    </div>

    <div class="letter__signature">Dane Holloway</div>

    <footer class="letter__footer">
      <div class="footer__name">Dane Holloway Naturopath</div>
      <div class="footer__details">
        <svg class="footer__icon" viewBox="0 0 10 10" aria-hidden="true"><path d="M5 0.5a3.3 3.3 0 0 0-3.3 3.3C1.7 6.3 5 9.5 5 9.5s3.3-3.2 3.3-5.7A3.3 3.3 0 0 0 5 0.5z" fill="var(--orange)"/><circle cx="5" cy="3.8" r="1.2" fill="#fff"/></svg>
        <span>Shop 3042c, 451 Marrow Lane, Sydney 2000</span>
        <svg class="footer__icon" viewBox="0 0 10 10" aria-hidden="true"><circle cx="5" cy="5" r="4.3" fill="none" stroke="var(--orange)" stroke-width="1"/><ellipse cx="5" cy="5" rx="1.8" ry="4.3" fill="none" stroke="var(--orange)" stroke-width="0.8"/><line x1="0.7" y1="5" x2="9.3" y2="5" stroke="var(--orange)" stroke-width="0.8"/></svg>
        <span>daneholloway.com.au</span>
        <span class="footer__social"></span>
        <span>marrowessences</span>
      </div>
    </footer>
  </section>

</main>
</body>
</html>
```